Harnacker TVK
Zielgruppe
Brauereien, Sekt und Weinhersteller, bzw. Getränkehersteller - Abfüller national und international
Aufgabenstellung
Aktuelles Briefpapier mit dem beigefügten neuen LOGO auf neuesten Stand bringen

```html
<!DOCTYPE html>
<html lang="de">
<head>
<meta charset="utf-8">
<title>Harnacker TVK – Briefbogen</title>
<link href="https://fonts.googleapis.com/css2?family=Mulish:wght@400;700&family=Source+Sans+3:wght@400;600&display=swap" rel="stylesheet">
<style>
  :root {
    --brand-blue: #1e7fe6;
    --ink: #1a1a1a;
    --footer-ink: #333333;
    --frame: #3a3a3a;
    --paper: #ffffff;
  }
  html, body {
    margin: 0;
    padding: 0;
    width: 1200px;
    height: 1190px;
    overflow: hidden;
    background: var(--paper);
  }
  .canvas {
    position: relative;
    width: 1200px;
    height: 1190px;
    background: var(--paper);
    font-family: "Mulish", sans-serif;
    color: var(--ink);
  }
  .sheet {
    position: absolute;
    left: 18px;
    top: 18px;
    width: 814px;
    height: 1150px;
    border: 2px solid var(--frame);
    box-sizing: border-box;
  }
  .brand {
    position: absolute;
    left: 592px;
    top: 52px;
    width: 160px;
    display: flex;
    flex-direction: column;
    align-items: flex-start;
    gap: 10px;
  }
  .brand-square {
    width: 22px;
    height: 22px;
    background: var(--brand-blue);
  }
  .brand-name {
    font-family: "Mulish", sans-serif;
    font-weight: 700;
    font-size: 24px;
    line-height: 28px;
    color: var(--brand-blue);
    letter-spacing: 0.5px;
    margin: 0;
  }
  .fold-mark {
    position: absolute;
    left: 18px;
    top: 427px;
    width: 18px;
    height: 18px;
    background: var(--brand-blue);
  }
  .sender-line {
    position: absolute;
    left: 97px;
    top: 205px;
    margin: 0;
    font-family: "Source Sans 3", sans-serif;
    font-size: 7.5px;
    color: var(--footer-ink);
    white-space: nowrap;
  }
  .sender-line .company { color: var(--brand-blue); font-weight: 600; }
  .text {
    position: absolute;
    left: 97px;
    font-size: 14.8px;
    line-height: 21px;
    margin: 0;
    white-space: nowrap;
  }
  .recipient { top: 236px; }
  .date {
    position: absolute;
    right: 477px;
    top: 399px;
    font-size: 14.8px;
    margin: 0;
    white-space: nowrap;
  }
  .subject { top: 440px; font-weight: 700; }
  .salutation { top: 479px; }
  .body-first { top: 522px; }
  .body-second { top: 644px; }
  .closing { top: 749px; }
  .signature {
    position: absolute;
    left: 72px;
    top: 770px;
    width: 80px;
    height: 38px;
  }
  .signatory { top: 812px; }
  .footer {
    position: absolute;
    left: 97px;
    font-family: "Source Sans 3", sans-serif;
    font-size: 9.5px;
    line-height: 15px;
    color: var(--footer-ink);
    margin: 0;
    white-space: nowrap;
  }
  .footer-contact { top: 1022px; }
  .footer-bank { top: 1088px; }
  .footer .company { color: var(--brand-blue); font-weight: 600; }
</style>
</head>
<body>
<div class="canvas">
  <div class="sheet"></div>

  <div class="brand">
    <span class="brand-square"></span>
    <p class="brand-name">HARNACKER<br>TVK</p>
  </div>

  <div class="fold-mark"></div>

  <p class="sender-line"><span class="company">Harnacker TVK Technik GmbH</span>&nbsp; Kornweg 14&nbsp; 79388 Talhausen</p>

  <p class="text recipient">Herrn Max Mustermann<br>Musterfirma GmbH<br>Musterstraße 1<br>12345 Musterstadt</p>

  <p class="date">Talhausen, 4. Juni 2009</p>

  <p class="text subject">Ihre Anfrage</p>

  <p class="text salutation">Sehr geehrter Herr Mustermann,</p>

  <p class="text body-first">si meliora dies, ut vina, poemata reddit, scire velim, chartis pretium quotus arroget annus.<br>Scriptor abhinc annos centum qui decidit, inter perfectos veteresque referri debet an inter<br>vilis atque novos? Excludat iurgia finis, Est vetus atque probus, centum qui perficit annos.<br>Quid, qui deperiit minor uno mense vel anno, inter quos referendus erit? Veteresne poetas,<br>an quos et praesens et postera respuat aetas?</p>

  <p class="text body-second">Iste quidem veteres inter ponetur honeste, qui vel mense brevi vel toto est iunior anno. Utor<br>permisso, caudaeque pilos ut equinae paulatim vello unum, demo etiam unum, dum cadat<br>elusus ratione ruentis acervi, qui redit in fastos et virtutem aestimat annis miraturque nihil<br>nisi quod Libitina sacravit.</p>

  <p class="text closing">Freundliche Grüße aus Talhausen</p>

  <svg class="signature" viewBox="0 0 80 38" role="img" aria-label="Handschriftliche Unterschrift der Geschäftsführung">
    <rect x="0" y="0" width="80" height="38" rx="6" fill="#1e7fe6" opacity="0.12"/>
  </svg>

  <p class="text signatory">Konrad Harnacker<br>Geschäftsführung</p>

  <p class="footer footer-contact"><span class="company">Harnacker TVK Technik GmbH</span>&nbsp; Geschäftsführung Konrad Harnacker<br>Kornweg 14&nbsp; 79388 Talhausen&nbsp; Germany&nbsp; Tel. +49 (0) 76 55 – 3 21 40 – 0&nbsp; Fax +49 (0) 76 55 – 3 21 40 – 200<br>info@harnacker-tvk.de&nbsp; www.harnacker-tvk.de</p>

  <p class="footer footer-bank">Kreissparkasse Talgau&nbsp; Konto 145 82 907&nbsp; BLZ 610 204 07&nbsp; IBAN DE 41 61 02 0407 0033 5192 07&nbsp; BIC KSTGDE61XXX<br>Nordbank Handelshaus AG&nbsp; Konto 0 442 917 000&nbsp; BLZ 620 300 11&nbsp; IBAN DE58 6203 0011 0442 9170 00&nbsp; BIC NBHADE6TXXX<br>Handelsregister Amtsgericht Talgau HRB 512 084&nbsp; USt-ID-Nummer DE 287 104 635</p>
</div>
</body>
</html>
```